Vello Shawarma Restaurant packging desgin

I want a packging desgin for my new Shawarma restaurant. The desgin should be modern and simple. I have added the logo and the identity in the attachment in PSD format so you can use it in the desgin. I also added some packging idea you may use it as background of your desgin. The main colors to be used is Red, grey, black and white.
Updates

Project Deadline Extended
Reason: Still i did not find an attractive desgin. I will try to provied you with feedback for each post

Target Market(s)

Food industry

Industry/Entity Type

Fast Food Restaurant

Font styles to use
Sans Serif

Colors
ec1f27
000000
919191
ffffff
eeeeee

Requirements
Must have
• The logo and the name VELLO. All boxes should be in the same theme
Nice to have
• Creative desgin and Twitter and instagram logo on the side
Should not have
• real food pictures

```html
<!DOCTYPE html>
<html lang="en">
<head>
<meta charset="utf-8">
<title>Vello Shawarma Restaurant – Packaging</title>
<link rel="stylesheet" href="https://fonts.googleapis.com/css2?family=Montserrat:wght@800&display=swap">
<style>
  :root {
    --red: #e30613;
    --red-band: #ec1f27;
    --grey: 166,167,169;
    --grey-light: 210,211,213;
    --grey-panel: #a9aaac;
    --white: #ffffff;
    --off-white: #f2f2f4;
    --backdrop: #cbcbcb;
  }
  * { margin: 0; padding: 0; box-sizing: border-box; }
  html, body { width: 1200px; height: 1200px; overflow: hidden; }
  body { background: var(--white); position: relative; font-family: "Montserrat", sans-serif; }

  .backdrop { position: absolute; left: 66px; top: 71px; width: 1066px; height: 1066px; background: var(--backdrop); }

  .piece { position: absolute; overflow: hidden; box-shadow: 2px 3px 6px rgba(0,0,0,0.18); }
  .wordmark {
    position: absolute; display: flex; align-items: center; gap: 8px; z-index: 2;
    font-weight: 800; letter-spacing: 0.02em; line-height: 1; white-space: nowrap;
  }
  .wordmark .dot { border-radius: 50%; display: block; }

  .brand-graphic { position: absolute; inset: 0; z-index: 1; }

  /* Wrap sleeve */
  .sleeve { left: 108px; top: 272px; width: 184px; height: 564px; background: var(--red); }
  .sleeve .top-fold { position: absolute; left: 0; top: 0; width: 100%; height: 32px; background: var(--white); z-index: 2; }
  .sleeve .wordmark { left: 36px; top: 66px; font-size: 20px; color: var(--white); }
  .sleeve .dot { width: 30px; height: 30px; background: var(--white); }
  .sleeve .brand-graphic {
    background: radial-gradient(ellipse 95% 30% at 0% 64%,
      rgba(var(--grey),1) 0%, rgba(var(--grey),0.9) 45%, rgba(var(--grey),0) 100%);
  }

  /* Carrier bag face */
  .bag { left: 318px; top: 266px; width: 466px; height: 414px; background: var(--red); }
  .bag .wordmark { left: 286px; top: 42px; font-size: 23px; color: var(--white); }
  .bag .dot { width: 34px; height: 34px; background: var(--white); }
  .bag .brand-graphic {
    background: radial-gradient(ellipse 58% 62% at 0% 42%,
      rgba(var(--grey),1) 0%, rgba(var(--grey),0.9) 45%, rgba(var(--grey),0) 100%);
  }

  /* Box lids */
  .box { width: 212px; height: 210px; }
  .box .wordmark { right: 16px; top: 12px; font-size: 17px; color: var(--red); }
  .box .dot { width: 26px; height: 26px; background: var(--red); }
  .band { position: absolute; left: 0; bottom: 0; width: 100%; height: 36px; background: var(--red-band); z-index: 2;
    clip-path: polygon(12% 0, 100% 0, 100% 100%, 0 100%); }
  .icons { position: absolute; right: 8px; bottom: 5px; display: flex; gap: 5px; z-index: 3; }
  .icons span { width: 26px; height: 26px; border-radius: 50%; border: 1.5px solid var(--white); display: block; }

  .box-grey { left: 828px; top: 256px; background: var(--grey-panel); }
  .box-grey .brand-graphic {
    background: radial-gradient(ellipse 75% 75% at 0% 30%,
      rgba(var(--grey-light),1) 0%, rgba(var(--grey-light),0.85) 45%, rgba(var(--grey-light),0) 100%);
  }

  .box-white { left: 828px; top: 486px; background: var(--white); }
  .box-white .brand-graphic,
  .box-flat .brand-graphic {
    background: radial-gradient(ellipse 72% 75% at 0% 30%,
      rgba(var(--grey),1) 0%, rgba(var(--grey),0.85) 45%, rgba(var(--grey),0) 100%);
  }

  .box-flat { left: 330px; top: 702px; width: 282px; height: 190px; background: var(--off-white); }
  .box-flat .wordmark { right: 12px; top: 24px; font-size: 20px; }
  .box-flat .dot { width: 30px; height: 30px; }
  .box-flat .band { height: 32px; clip-path: polygon(10% 0, 100% 0, 100% 100%, 0 100%); }
  .box-flat .icons span { width: 24px; height: 24px; }
</style>
</head>
<body>
  <div class="backdrop"></div>

  <section class="piece sleeve" aria-label="Wrap sleeve">
    <div class="top-fold"></div>
    <div class="brand-graphic" role="img" aria-label="Large grey brand swoosh graphic"></div>
    <div class="wordmark">VELLO<span class="dot"></span></div>
  </section>

  <section class="piece bag" aria-label="Carrier bag">
    <div class="brand-graphic" role="img" aria-label="Large grey brand swoosh graphic"></div>
    <div class="wordmark">VELLO<span class="dot"></span></div>
  </section>

  <section class="piece box box-grey" aria-label="Grey box lid">
    <div class="brand-graphic" role="img" aria-label="Light grey brand swoosh graphic"></div>
    <div class="wordmark">VELLO<span class="dot"></span></div>
    <div class="band"></div>
    <div class="icons" role="img" aria-label="Menu item icons: skewer, wrap, pita"><span></span><span></span><span></span></div>
  </section>

  <section class="piece box box-white" aria-label="White box lid">
    <div class="brand-graphic" role="img" aria-label="Grey brand swoosh graphic"></div>
    <div class="wordmark">VELLO<span class="dot"></span></div>
    <div class="band"></div>
    <div class="icons" role="img" aria-label="Menu item icons: skewer, wrap, pita"><span></span><span></span><span></span></div>
  </section>

  <section class="piece box box-flat" aria-label="Meal box lid">
    <div class="brand-graphic" role="img" aria-label="Grey brand swoosh graphic"></div>
    <div class="wordmark">VELLO<span class="dot"></span></div>
    <div class="band"></div>
    <div class="icons" role="img" aria-label="Menu item icons: skewer, wrap, pita"><span></span><span></span><span></span></div>
  </section>
</body>
</html>
```